Business card design needed

A small accounting firm that has relocated from the regional areas of Australia, to be city based, and using the resources of The Cloud to remake and streamline its operations, and wanting to share the benefits with small businesses all over Australia. We provide services on a fixed price basis, and run regular events for clients and potential clients.

Major product partners are Quorel Ledgering, Gatherloom, SlotFinch, Tallo and Pagemoss.

Please review the update to the brief.

Thanks.

Reason: Just swamped by good designs, need more time to provide feedback and make choices. Thanks in advance for the great efforts so far!

Need cards for 2 people

1. Dennis Halvorsen, Development Director
Mobile - 0499 572 438
dennis@fernbrookledger.example

2. Ruth Okonedo, Accountant
Mobile - 0488 164 729
ruth@fernbrookledger.example

Please check the amendments to the brief regarding web address etc.

Reason: Wanting some revisions before final selection.

Target Market(s)

Micro and Small business owners, trades, service and hospitality industries. Web savvy.

Industry/Entity Type

Accounting

Contact Information for Business Card

Fernbrook Ledger,
Level 5, Harwick Lane Plaza,
127 Harwick Lane, Melbourne, 3000

Logo Text

Fernbrook Ledger - Ledger Accounting and Business Solutions

Logo styles of interest
Abstract Logo
Requirements
Must have
• Must include some tagline for our services - eg Accounting & Business services, Fixed Price, Tax

On Reverse side
Twitter Address - @FernbrookLedgerAu
Facebook - www.socialpage.example/FernbrookLedger
Book Online Appointment (Slot Finch) - www.shortlink.example/ledgerslot
Nice to have
• The Quorel Logo - We are a Quorel Partner. Guidelines for logo use have been uploaded.

```html
<!DOCTYPE html>
<html lang="en">
<head>
<meta charset="utf-8">
<title>Fernbrook Ledger – Business Card</title>
<link href="https://fonts.googleapis.com/css2?family=Open+Sans:wght@400;700&display=swap" rel="stylesheet">
<style>
  :root {
    --card-bg: #ffffff;
    --card-border: #c9c9c9;
    --brand-blue: #1a72b8;
    --brand-navy: #1b4d8c;
    --text-dark: #1e1e1e;
    --text-grey: #6d6d6d;
    --divider: #b8b8b8;
  }
  * { margin: 0; padding: 0; box-sizing: border-box; }
  html, body {
    width: 1200px;
    height: 695px;
    overflow: hidden;
    background: var(--card-bg);
    font-family: "Open Sans", sans-serif;
  }
  .business-card {
    position: relative;
    width: 1200px;
    height: 695px;
    background: var(--card-bg);
    border: 2px solid var(--card-border);
  }
  .brand {
    position: absolute;
    left: 62px;
    top: 222px;
    display: flex;
    align-items: center;
    gap: 22px;
  }
  .brand-dot {
    width: 118px;
    height: 118px;
    border-radius: 50%;
    background: var(--brand-blue);
    flex: none;
  }
  .brand-name {
    color: var(--brand-navy);
    font-weight: 700;
    font-size: 46px;
    line-height: 1.05;
  }
  .divider {
    position: absolute;
    left: 570px;
    top: 162px;
    width: 40px;
    height: 264px;
  }
  .contact {
    position: absolute;
    left: 700px;
    top: 208px;
  }
  .contact-name {
    color: var(--brand-blue);
    font-size: 32px;
    font-weight: 400;
    line-height: 1.1;
  }
  .contact-role {
    color: var(--text-grey);
    font-size: 23px;
    line-height: 1.2;
    margin-bottom: 14px;
  }
  .contact-line {
    display: flex;
    align-items: center;
    gap: 12px;
    color: var(--text-dark);
    font-size: 28px;
    line-height: 1.5;
  }
  .contact-icon {
    width: 22px;
    height: 26px;
    flex: none;
  }
  .tagline {
    position: absolute;
    left: 0;
    right: 0;
    top: 484px;
    text-align: center;
    color: var(--brand-blue);
    font-size: 33px;
  }
</style>
</head>
<body>
  <main class="business-card">
    <div class="brand">
      <span class="brand-dot"></span>
      <div class="brand-name">Fernbrook<br>Ledger</div>
    </div>

    <svg class="divider" viewBox="0 0 40 264" aria-hidden="true">
      <polyline points="6,0 6,162 28,184 6,206 6,264" fill="none" stroke="var(--divider)" stroke-width="2"/>
    </svg>

    <section class="contact">
      <h1 class="contact-name">Dennis Halvorsen</h1>
      <p class="contact-role">(Development Director)</p>
      <p class="contact-line">
        <svg class="contact-icon" viewBox="0 0 22 26" aria-hidden="true">
          <rect x="4" y="1" width="14" height="24" rx="2.5" fill="none" stroke="var(--brand-blue)" stroke-width="2.5"/>
          <line x1="9" y1="21" x2="13" y2="21" stroke="var(--brand-blue)" stroke-width="2"/>
        </svg>
        0499 572 438
      </p>
      <p class="contact-line">
        <svg class="contact-icon" viewBox="0 0 22 26" aria-hidden="true">
          <path d="M1 11 L11 4 L21 11 V23 H1 Z" fill="var(--brand-blue)"/>
          <path d="M1 11 L11 18 L21 11" fill="none" stroke="#ffffff" stroke-width="1.8"/>
        </svg>
        dennis@fernbrookledger.example
      </p>
    </section>

    <p class="tagline">Accounting &amp; Business Services, Fixed Price, Tax</p>
  </main>
</body>
</html>
```